Property investment company needs a letterhead design!

We are a new residential and commercial property investment company. Name of the company is Morvessa Group, LLC. We have a new logo and now we need letterhead! We prefer to have a professional and upscale appearance. We don't have any fixed requirements, so be creative! Thank you for considering this project. We are so excited to see what happens!

Target Market(s)

Professional

Industry/Entity Type

Real Estate Development

```html
<!DOCTYPE html>
<html lang="en">
<head>
<meta charset="utf-8">
<title>Morvessa Group, LLC – Stationery</title>
<link rel="stylesheet" href="https://fonts.googleapis.com/css2?family=Open+Sans:wght@400;600;700&family=Roboto:wght@400;500&display=swap">
<style>
  :root {
    --navy: #0c1f3d;
    --sky: #1ba5e3;
    --ink: #3a3d42;
    --muted: #5b5f66;
    --paper: #ffffff;
    --backdrop: #e9eaec;
  }
  * { box-sizing: border-box; margin: 0; padding: 0; }
  html, body { width: 1200px; height: 800px; overflow: hidden; }
  body {
    background: var(--backdrop);
    font-family: "Open Sans", Arial, sans-serif;
    color: var(--ink);
    position: relative;
  }
  .letterhead {
    position: absolute;
    left: 90px; top: 40px;
    width: 510px; height: 720px;
    background: var(--paper);
    box-shadow: 0 4px 18px rgba(0,0,0,0.12);
    overflow: hidden;
  }
  .brand {
    position: absolute;
    display: flex; align-items: center; gap: 7px;
    font-family: "Open Sans", Arial, sans-serif;
    font-weight: 700;
    color: var(--navy);
    letter-spacing: 0.04em;
    white-space: nowrap;
  }
  .brand-dot {
    display: inline-block;
    border-radius: 50%;
    background: var(--sky);
  }
  .letterhead .brand { left: 48px; top: 44px; font-size: 15px; }
  .letterhead .brand-dot { width: 14px; height: 14px; }
  .contact {
    position: absolute;
    right: 48px; top: 112px;
    font-family: "Roboto", Arial, sans-serif;
    font-size: 8.5px;
    line-height: 1.45;
    color: var(--muted);
  }
  .contact-name { color: var(--sky); font-weight: 500; }
  .contact-line { display: flex; align-items: center; gap: 4px; }
  .contact-line svg { width: 8px; height: 8px; fill: var(--sky); flex: none; }
  .letter-body {
    position: absolute;
    left: 48px; right: 48px; top: 176px;
    font-size: 8.5px;
    line-height: 1.6;
    color: var(--ink);
  }
  .salutation { margin-bottom: 12px; }
  .letter-body p.paragraph { margin-bottom: 12px; }
  .closing { margin-top: 4px; }
  .signature {
    width: 70px; height: 44px; margin-top: 10px;
    background: linear-gradient(135deg, #f1f2f4, #e3e5e8);
    border-radius: 3px;
  }
  .footer-band {
    position: absolute;
    left: 0; bottom: 0;
    width: 510px; height: 40px;
  }
  .footer-url {
    position: absolute;
    right: 40px; bottom: 7px;
    font-size: 10px;
    color: #ffffff;
    letter-spacing: 0.02em;
  }
  .card {
    position: absolute;
    width: 200px; height: 330px;
    box-shadow: 0 4px 14px rgba(0,0,0,0.14);
    display: flex; align-items: center; justify-content: center;
  }
  .card .brand { position: static; font-size: 13px; }
  .card .brand-dot { width: 12px; height: 12px; }
  .card-light { left: 690px; top: 235px; background: var(--paper); }
  .card-dark { left: 930px; top: 235px; background: var(--navy); }
  .card-dark .brand { color: #ffffff; }
</style>
</head>
<body>
  <section class="letterhead">
    <div class="brand"><span class="brand-dot"></span>MORVESSA GROUP, LLC</div>

    <address class="contact">
      <div class="contact-name">Morvessa Group, LLC</div>
      <div>PO Box 4821 Harlow Bay</div>
      <div>NSW 2200</div>
      <div class="contact-line">
        <svg viewBox="0 0 24 24"><path d="M6.6 10.8a15.1 15.1 0 0 0 6.6 6.6l2.2-2.2a1 1 0 0 1 1-.25 11.4 11.4 0 0 0 3.6.57 1 1 0 0 1 1 1V20a1 1 0 0 1-1 1A17 17 0 0 1 3 4a1 1 0 0 1 1-1h3.5a1 1 0 0 1 1 1c0 1.25.2 2.45.57 3.57a1 1 0 0 1-.25 1z"/></svg>
        +55510284736
      </div>
      <div class="contact-line">
        <svg viewBox="0 0 24 24"><path d="M2 5h20v14H2z M2 5l10 8 10-8" /></svg>
        info@morvessagroup.com
      </div>
    </address>

    <div class="letter-body">
      <p class="salutation">Dear customer,</p>
      <p class="paragraph">Lorem ipsum dolor sit amet, consectetur adipisicing elit, sed do eiusmod tempor incididunt ut labore et dolore magna aliqua. Ut enim ad minim veniam, quis nostrud exercitation ullamco laboris nisi ut aliquip ex ea commodo consequat. Duis aute irure dolor in reprehenderit in voluptate velit esse cillum dolore eu fugiat nulla pariatur. Excepteur sint occaecat cupidatat non proident, sunt in culpa qui officia deserunt mollit anim id est laborum.</p>
      <p class="paragraph">Lorem ipsum dolor sit amet, consectetur adipisicing elit, sed do eiusmod tempor incididunt ut labore et dolore magna aliqua. Ut enim ad minim veniam, quis nostrud exercitation ullamco laboris nisi ut aliquip ex ea commodo consequat. Duis aute irure dolor in reprehenderit in voluptate velit esse cillum dolore eu fugiat nulla pariatur. Excepteur sint occaecat cupidatat non proident, sunt in culpa qui officia deserunt mollit anim id est laborum.</p>
      <p class="paragraph">Lorem ipsum dolor sit amet, consectetur adipisicing elit, sed do eiusmod tempor incididunt ut labore et dolore magna aliqua. Ut enim ad minim veniam, quis nostrud exercitation ullamco laboris nisi ut aliquip ex ea commodo consequat. Duis aute irure dolor in reprehenderit in voluptate velit esse cillum dolore eu fugiat nulla pariatur. Excepteur sint occaecat cupidatat non proident, sunt in culpa qui officia deserunt mollit anim id est laborum.</p>
      <p class="paragraph">Lorem ipsum dolor sit amet, consectetur adipisicing elit, sed do eiusmod tempor incididunt ut labore et dolore magna aliqua. Ut enim ad minim veniam, quis nostrud exercitation ullamco laboris nisi ut aliquip ex ea commodo consequat. Duis aute irure dolor in reprehenderit.</p>
      <p class="closing">Yours Sincerely,</p>
      <div class="signature" role="img" aria-label="Handwritten signature"></div>
    </div>

    <svg class="footer-band" viewBox="0 0 510 40" aria-hidden="true">
      <rect x="0" y="34" width="510" height="6" fill="#0c1f3d"/>
      <polygon points="300,40 318,16 510,16 510,40" fill="#1ba5e3"/>
    </svg>
    <div class="footer-url">www.morvessagroup.com</div>
  </section>

  <section class="card card-light">
    <div class="brand"><span class="brand-dot"></span>MORVESSA GROUP, LLC</div>
  </section>

  <section class="card card-dark">
    <div class="brand"><span class="brand-dot"></span>MORVESSA GROUP, LLC</div>
  </section>
</body>
</html>
```